Looking for a modern elegant home improvment website

Looking for a new Design on current website . Please us www.larkfieldbuilders.example PIctures of recent work and stock photos that were attached , Free estimates , Explaining what we do , Similiar to www. larkfieldbuilders.example which is our current webpage . Colors can be different . I have attached our buisness card as well as our postcard we send out to homes . I would like a modern web page that our costumers can feel is professional so they can have a feeling of trust when they hire us . Our address should be on there . Licenesed & Insured should be somewhere on the page . Our Company Logo should be there as well . It would be nice to have a very modern website with great pictures of home interiors and exteriors . a page describing what we do is very important . facebook link to our page is a must as well as a instagram .
Updates

Reason: Looking for a elegant modern 5 page website with proper spelling and professional looking . I extended the deadline and upgraded .

Reason: Looking for more design options .

Target Market(s)

Home owners , Commerical buisness,

Industry/Entity Type

Home Improvement

Number of Pages Required

5+ page

Font styles to use
Serif

Requirements
Must have
• PIctures of recent work and stock photos that were attached , Free estimates , Explaining what we do , Similiar to www. larkfieldbuilders.example which is our current webpage . Colors can be different . I have attached our buisness card as well as our postcard we send out to homes . I would like a modern web page that our costumers can feel is professional so they can have a feeling of trust when they hire us . Our address should be on there . Licenesed & Insured should be somewhere on the page . Our Company Logo should be there as well .
Nice to have
• It would be nice to have a very modern website with great pictures of home interiors and exteriors . a page describing what we do is very important . facebook link to our page is a must as well as a instagram .

```html
<!DOCTYPE html>
<html lang="en">
<head>
<meta charset="utf-8">
<title>Larkfield Builders LLC — Home Improvement</title>
<link href="https://fonts.googleapis.com/css2?family=Open+Sans:ital,wght@0,400;0,600;0,700;1,400&family=Raleway:wght@400;500;600&display=swap" rel="stylesheet">
<style>
:root{
  --green:#0f8446;
  --green-dark:#0a5c2e;
  --green-band:#11884a;
  --ink:#333;
  --muted:#777;
  --soft:#f2f2f2;
  --white:#fff;
  --line:#dcdcdc;
}
*{box-sizing:border-box;margin:0;padding:0}
html,body{width:1200px;height:3158px;overflow:hidden}
body{font-family:"Open Sans",Arial,sans-serif;color:var(--ink);background:var(--white);position:relative}
h1,h2,h3{font-weight:400}
.section{position:absolute;left:0;width:1200px}
.abs{position:absolute}
.center{text-align:center}

/* header */
.site-header{top:0;height:143px;background:var(--white)}
.brand{left:100px;top:44px;display:flex;align-items:center;gap:14px}
.brand-mark{width:26px;height:26px;background:var(--green)}
.brand-name{font-family:"Raleway",sans-serif;font-weight:600;font-size:26px;color:var(--green-dark);letter-spacing:.5px}
.contact-item{top:58px;display:flex;align-items:flex-start;gap:16px;font-size:15px;line-height:21px;color:#222}
.contact-icon{width:38px;height:38px;border:2px solid var(--green-dark);display:flex;align-items:center;justify-content:center;border-radius:3px}
.contact-phone{left:616px}
.contact-address{left:922px}

/* nav */
.main-nav{top:143px;height:57px;background:var(--green-dark);display:flex;justify-content:center;align-items:center;gap:52px}
.main-nav a{color:var(--white);text-decoration:none;font-size:15px}

/* hero */
.hero{top:200px;height:463px;background:linear-gradient(135deg,#7a4a22 0%,#a8703a 35%,#5c3418 70%,#8a5a2e 100%)}
.hero-shade{inset:0;background:rgba(0,0,0,.25)}
.hero-title{top:150px;width:100%;font-size:42px;font-weight:600;color:var(--white)}
.hero-sub{top:214px;width:100%;font-size:18px;font-weight:700;line-height:26px;color:var(--white)}
.dots{display:flex;gap:10px;justify-content:center;width:100%}
.dot{width:11px;height:11px;border-radius:50%;background:#999}
.dot.on{background:var(--green)}
.hero .dots{top:406px}
.hero .dot{background:rgba(255,255,255,.6)}
.hero .dot.on{background:var(--green)}

/* intro */
.intro{top:663px;height:255px}
.intro-col{top:66px;width:300px}
.intro-col h2{font-family:"Raleway",sans-serif;font-weight:400;font-size:22px;color:#444;margin-bottom:24px}
.intro-col p{font-size:12px;line-height:21px;color:var(--muted)}

/* stats */
.stats{top:918px;height:128px;background:var(--green-band);display:flex}
.stat{height:100%;display:flex;flex-direction:column;align-items:center;justify-content:center;color:var(--white);border-right:2px solid rgba(255,255,255,.55)}
.stat:last-child{border-right:none}
.stat-num{font-size:46px;letter-spacing:8px;font-weight:400;line-height:50px}
.stat-label{font-size:13px;font-weight:600;margin-top:12px;text-transform:uppercase}

/* services */
.services{top:1046px;height:739px;background:var(--soft);border-left:4px solid #e2e2e2}
.worker-photo{left:84px;top:28px;width:305px;height:663px;background:linear-gradient(180deg,#f2c230 0%,#f2c230 12%,#e8d8a0 22%,#2c3340 40%,#2c3340 100%);border-radius:120px 120px 20px 20px}
.services-title{left:420px;top:88px;width:714px;font-family:"Raleway",sans-serif;font-weight:400;font-size:36px;color:#333}
.services-lead{left:470px;top:142px;width:614px;font-size:14px;line-height:23px;color:var(--muted)}
.service{width:170px;display:flex;flex-direction:column;align-items:center}
.service-icon{width:78px;height:78px;border-radius:50%;border:2px dashed var(--green);display:flex;align-items:center;justify-content:center}
.service-name{margin-top:16px;font-size:24px;color:#444;white-space:nowrap}
.services .dots{left:420px;width:714px;top:656px}

/* featured */
.featured{top:1785px;height:598px}
.featured-title{top:42px;width:100%;font-family:"Raleway",sans-serif;font-weight:400;font-size:36px;color:#444}
.featured-sub{top:96px;width:100%;font-family:"Raleway",sans-serif;font-size:25px;color:#444}
.work{top:156px;width:280px}
.work-photo{width:280px;height:204px;position:relative}
.work-photo .frame{position:absolute;left:10px;top:14px;width:246px;height:178px;border:2px solid var(--green)}
.work h3{font-family:"Raleway",sans-serif;font-weight:500;font-size:26px;margin-top:12px;color:#222}
.work p{font-size:13px;line-height:22px;color:#555;margin-top:4px}
.btn{display:flex;align-items:center;justify-content:center;gap:12px;font-size:19px;text-decoration:none}
.btn-green{left:484px;top:491px;width:232px;height:57px;background:var(--green);color:var(--white)}

/* testimonials */
.testimonials{top:2383px;height:446px;background:var(--soft)}
.t-title{top:34px;width:100%;font-family:"Raleway",sans-serif;font-weight:400;font-size:34px;color:#444;text-transform:uppercase}
.t-sub{top:86px;width:100%;font-family:"Raleway",sans-serif;font-size:19px;color:#555}
.card{top:149px;width:352px;height:223px;background:var(--white);box-shadow:0 1px 4px rgba(0,0,0,.08);padding:64px 22px 0}
.avatar{left:156px;top:-6px;width:40px;height:46px;border-radius:50%;background:#a07860}
.quote-mark{left:20px;top:22px;font-size:32px;color:#ddd;font-family:"Raleway",sans-serif}
.card-name{font-family:"Raleway",sans-serif;font-size:15px;color:#555;text-align:center}
.card-role{font-size:8px;color:#999;text-align:center;margin:2px 0 10px}
.card-text{font-size:10px;font-style:italic;line-height:16px;color:#555}
.testimonials .dots{top:407px}

/* cta */
.cta{top:2829px;height:246px;background:var(--green)}
.cta-rule{left:0;width:1200px;border-top:2px dashed rgba(255,255,255,.75)}
.cta-title{top:56px;width:100%;font-family:"Raleway",sans-serif;font-weight:400;font-size:30px;color:var(--white);text-transform:uppercase}
.cta-sub{top:104px;width:100%;font-size:22px;font-weight:600;color:var(--white);text-transform:uppercase}
.btn-white{left:495px;top:156px;width:212px;height:57px;background:var(--white);color:var(--green)}

/* footer */
.site-footer{top:3075px;height:83px;background:#f4f4f4;font-size:14px;color:#444}
.follow{left:48px;top:36px;display:flex;align-items:center;gap:14px;font-style:italic;font-weight:600}
.social{width:16px;height:16px;border-radius:50%;background:#555}
.copyright{left:430px;top:38px}
.subscribe{left:828px;top:40px}
.subscribe a{color:#444}
</style>
</head>
<body>

<header class="section site-header">
  <div class="abs brand"><span class="brand-mark"></span><span class="brand-name">Larkfield Builders LLC</span></div>
  <div class="abs contact-item contact-phone">
    <span class="contact-icon"><svg width="20" height="20" viewBox="0 0 24 24"><path d="M6.6 10.8a15 15 0 0 0 6.6 6.6l2.2-2.2c.3-.3.7-.4 1-.2 1.1.4 2.3.6 3.6.6.6 0 1 .4 1 1V20c0 .6-.4 1-1 1A17 17 0 0 1 3 4c0-.6.4-1 1-1h3.5c.6 0 1 .4 1 1 0 1.3.2 2.5.6 3.6.1.3 0 .7-.2 1z" fill="none" stroke="#0a5c2e" stroke-width="2"/></svg></span>
    <span>555 014 2290<br>hello@larkfieldbuilders.example</span>
  </div>
  <div class="abs contact-item contact-address">
    <span class="contact-icon"><svg width="20" height="20" viewBox="0 0 24 24"><path d="M12 2a7 7 0 0 0-7 7c0 5 7 13 7 13s7-8 7-13a7 7 0 0 0-7-7z" fill="none" stroke="#0a5c2e" stroke-width="2"/><circle cx="12" cy="9" r="2.5" fill="#0a5c2e"/></svg></span>
    <span>48 Orchard Lane<br>Millbrook, NJ 07999</span>
  </div>
</header>

<nav class="section main-nav">
  <a href="#">Home</a><a href="#">About Us</a><a href="#">Services</a><a href="#">Portfolio</a><a href="#">Testimonials</a><a href="#">Contact Us</a>
</nav>

<section class="section hero" role="img" aria-label="Photo of a remodelled kitchen with wood cabinets and granite counters">
  <div class="abs hero-shade"></div>
  <h1 class="abs hero-title center">Free Estimates - Licensed &amp; Fully Insured</h1>
  <p class="abs hero-sub center">Your home is the most important asset you have, so when you're ready to build or remodel,<br>get yourself the best General Contractor in the business!</p>
  <div class="abs dots"><span class="dot on"></span><span class="dot"></span><span class="dot"></span><span class="dot"></span></div>
</section>

<section class="section intro">
  <div class="abs intro-col" style="left:116px">
    <h2>Our Mission</h2>
    <p>Your home is the most important asset you have, so when you're ready to build or remodel, get yourself the best General Contractor in the business!</p>
  </div>
  <div class="abs intro-col" style="left:455px">
    <h2>What We Do</h2>
    <p>We build bathrooms , Kitchens , Additions and much more . Give us a try , we do great work and are very passionate about what we do.</p>
  </div>
  <div class="abs intro-col" style="left:789px">
    <h2>Why Choose Us</h2>
    <p>We are a family owned business that has been in the construction field for over 20 years . Free Estimates - Licensed &amp; Fully insured.</p>
  </div>
</section>

<section class="section stats">
  <div class="stat" style="width:318px"><span class="stat-num">20</span><span class="stat-label">Years of Experience</span></div>
  <div class="stat" style="width:284px"><span class="stat-num">30</span><span class="stat-label">Built Housing Estates</span></div>
  <div class="stat" style="width:246px"><span class="stat-num">15</span><span class="stat-label">Qualified Specialists</span></div>
  <div class="stat" style="width:352px"><span class="stat-num">25</span><span class="stat-label">Built and Enhanced Designs</span></div>
</section>

<section class="section services">
  <div class="abs worker-photo" role="img" aria-label="Photo of a builder in a hard hat, yellow shirt and overalls with a tool belt"></div>
  <h2 class="abs services-title center">Our Services</h2>
  <p class="abs services-lead center">Give us a try, we do great work and are very passionate about whatwe do. We are a family owned business that has been in the construction field for over 20 years.</p>

  <div class="abs service" style="left:382px;top:258px">
    <span class="service-icon"><svg width="40" height="40" viewBox="0 0 40 40"><path d="M30 6l4 4-14 14-4-4z" fill="#0f8446"/><path d="M14 22l4 4c-2 5-7 7-12 6 3-2 3-6 8-10z" fill="#0f8446"/></svg></span>
    <span class="service-name">Painting</span>
  </div>
  <div class="abs service" style="left:582px;top:258px">
    <span class="service-icon"><svg width="40" height="40" viewBox="0 0 40 40"><rect x="8" y="16" width="24" height="16" rx="3" fill="#0f8446"/><rect x="4" y="14" width="32" height="3" fill="#0f8446"/><rect x="17" y="9" width="6" height="4" fill="#0f8446"/></svg></span>
    <span class="service-name">Kitchens</span>
  </div>
  <div class="abs service" style="left:778px;top:258px">
    <span class="service-icon"><svg width="40" height="40" viewBox="0 0 40 40"><rect x="6" y="24" width="18" height="8" fill="#0f8446"/><circle cx="10" cy="34" r="2.5" fill="#0f8446"/><circle cx="20" cy="34" r="2.5" fill="#0f8446"/><path d="M20 24L28 10l6 8" stroke="#0f8446" stroke-width="3" fill="none"/><rect x="30" y="18" width="6" height="8" fill="#0f8446"/></svg></span>
    <span class="service-name">Demolition</span>
  </div>
  <div class="abs service" style="left:959px;top:258px">
    <span class="service-icon"><svg width="40" height="40" viewBox="0 0 40 40"><path d="M5 20h30v4a8 8 0 0 1-8 8H13a8 8 0 0 1-8-8z" fill="#0f8446"/><path d="M10 20V9a3 3 0 0 1 6 0" stroke="#0f8446" stroke-width="2.5" fill="none"/></svg></span>
    <span class="service-name">Bathrooms</span>
  </div>
  <div class="abs service" style="left:382px;top:466px">
    <span class="service-icon"><svg width="40" height="40" viewBox="0 0 40 40"><path d="M4 20l10-10 10 10-10 10z" fill="none" stroke="#0f8446" stroke-width="3"/><path d="M18 10l10 10-10 10M24 10l10 10-10 10" fill="none" stroke="#0f8446" stroke-width="3"/></svg></span>
    <span class="service-name">Tile &amp; Marble</span>
  </div>
  <div class="abs service" style="left:582px;top:466px">
    <span class="service-icon"><svg width="40" height="40" viewBox="0 0 40 40"><path d="M6 34V8l28 0v26z" fill="none" stroke="#0f8446" stroke-width="2.5"/><path d="M10 34v-6h6v-6h6v-6h6v18z" fill="#0f8446"/></svg></span>
    <span class="service-name">Basements</span>
  </div>
  <div class="abs service" style="left:778px;top:466px">
    <span class="service-icon"><svg width="40" height="40" viewBox="0 0 40 40"><ellipse cx="14" cy="14" rx="5" ry="8" fill="#0f8446"/><ellipse cx="26" cy="24" rx="5" ry="8" fill="#0f8446"/><rect x="10" y="24" width="8" height="4" fill="#0f8446"/><rect x="22" y="34" width="8" height="3" fill="#0f8446"/></svg></span>
    <span class="service-name">Steps</span>
  </div>
  <div class="abs service" style="left:959px;top:466px">
    <span class="service-icon"><svg width="40" height="40" viewBox="0 0 40 40"><path d="M8 32l14-14 6 6-14 14z" fill="#0f8446"/><path d="M26 14l6-6" stroke="#0f8446" stroke-width="3"/></svg></span>
    <span class="service-name">Pavers</span>
  </div>

  <div class="abs dots"><span class="dot on"></span><span class="dot"></span><span class="dot"></span><span class="dot"></span></div>
</section>

<section class="section featured">
  <h2 class="abs featured-title center">Featured Work</h2>
  <p class="abs featured-sub center">We Take Pride In Our Work</p>
  <article class="abs work" style="left:149px">
    <div class="work-photo" role="img" aria-label="Photo of a kitchen with black granite counters and light wood cabinets" style="background:linear-gradient(160deg,#6b2f1e,#2a1a14 50%,#d9b27c)"><span class="frame"></span></div>
    <h3>Kitchen</h3>
    <p>Lorem Ipsum is simply dummy text of the printing and typesetting industry.</p>
  </article>
  <article class="abs work" style="left:461px">
    <div class="work-photo" role="img" aria-label="Photo of a bathroom with a marble-tiled tub surround" style="background:linear-gradient(160deg,#8a5a2c,#c9a06a 50%,#e8dcc8)"><span class="frame"></span></div>
    <h3>Bathroom</h3>
    <p>Lorem Ipsum is simply dummy text of the printing and typesetting industry.</p>
  </article>
  <article class="abs work" style="left:775px">
    <div class="work-photo" role="img" aria-label="Photo of a house exterior with new white railed steps" style="background:linear-gradient(180deg,#4f6d3a,#c9ccc4 45%,#f0f0f0)"></div>
    <h3>Steps</h3>
    <p>Lorem Ipsum is simply dummy text of the printing and typesetting industry.</p>
  </article>
  <a class="abs btn btn-green" href="#">View Portfolio <svg width="20" height="18" viewBox="0 0 20 18"><rect x="1" y="5" width="18" height="12" rx="2" fill="#fff"/><rect x="7" y="1" width="6" height="5" rx="1" fill="none" stroke="#fff" stroke-width="2"/></svg></a>
</section>

<section class="section testimonials">
  <h2 class="abs t-title center">What Our Clients Are Saying</h2>
  <p class="abs t-sub center">Don't Just Take Our World</p>
  <article class="abs card" style="left:232px">
    <span class="abs avatar" role="img" aria-label="Client portrait photo"></span>
    <span class="abs quote-mark">&ldquo;</span>
    <p class="card-name">Jane Doe</p>
    <p class="card-role">Home Owner</p>
    <p class="card-text">From the first visit to the final walkthrough the crew was punctual, tidy and honest about every cost. Our kitchen was finished on schedule and the work shows real care. We have already recommended them to our neighbors and will call again for the basement next spring.</p>
  </article>
  <article class="abs card" style="left:610px">
    <span class="abs avatar" role="img" aria-label="Client portrait photo" style="background:#9aa0a8"></span>
    <span class="abs quote-mark">&ldquo;</span>
    <p class="card-name">John Doe</p>
    <p class="card-role">Business Owner</p>
    <p class="card-text">They rebuilt the entrance steps and pavers at our shop front in under a week while we stayed open. The team kept the site safe, cleaned up each evening and explained every choice. Clear pricing, solid results and a crew that clearly takes pride in the job.</p>
  </article>
  <div class="abs dots"><span class="dot on"></span><span class="dot"></span><span class="dot"></span><span class="dot"></span></div>
</section>

<section class="section cta">
  <div class="abs cta-rule" style="top:28px"></div>
  <h2 class="abs cta-title center">We Can Help Build Your Project!</h2>
  <p class="abs cta-sub center">Tell Us About Our Project</p>
  <a class="abs btn btn-white" href="#">Contact Us <svg width="20" height="16" viewBox="0 0 20 16"><rect x="1" y="1" width="18" height="14" rx="1" fill="none" stroke="#0f8446" stroke-width="2"/><path d="M1 2l9 7 9-7" fill="none" stroke="#0f8446" stroke-width="2"/></svg></a>
  <div class="abs cta-rule" style="top:228px"></div>
</section>

<footer class="section site-footer">
  <div class="abs follow">Follow Us: <span class="social" role="img" aria-label="Social media link"></span><span class="social" role="img" aria-label="Social media link"></span></div>
  <p class="abs copyright">© 2017 Larkfieldbuilders.  Al Rights Reserved</p>
  <p class="abs subscribe">Subscribe: <a href="#">Feeds</a> | <a href="#">Newsletters</a> | <a href="#">Podcasts</a> | <a href="#">Apps</a></p>
</footer>

</body>
</html>
```